Bright Anchor Tools and Building Supply Inc. (Rebranding)

Target Market(s)

mainly people who do DIY, and also construction companies.

Industry/Entity Type

Construction

Contact Information for Business Card

418 R. Velasco St. Brgy. 164 Sta. Lucia Manila, Philippines 1003
(02) 861-4097
www.bat.example
brightanchortools@mailbox.example

Number of Pages Required

5+ page

Font styles to use
Sans Serif

Colors
f37122
f78f20

Requirements
Must have
• to RETAIN the current logo used.
Nice to have
• ideas on how to apply the current logos to different promotional items
Should not have
• DO NOT change the Current Logo

```html
<!DOCTYPE html>
<html lang="en">
<head>
<meta charset="utf-8">
<title>Bright Anchor Tools and Building Supply Inc. — Stationery Set</title>
<link rel="stylesheet" href="https://fonts.googleapis.com/css2?family=Montserrat:wght@800&family=Roboto:wght@400;700&display=swap">
<style>
  :root {
    --orange: #f37122;
    --orange-light: #f78f20;
    --paper: #ffffff;
    --backdrop: #d8d8d8;
    --ink: #1e1e1e;
    --accent-red: #d9141e;
  }
  * { box-sizing: border-box; margin: 0; padding: 0; }
  html, body { width: 1200px; height: 1200px; overflow: hidden; }
  body {
    background: var(--backdrop);
    position: relative;
    font-family: "Roboto", Arial, sans-serif;
  }
  .sheet { position: absolute; box-shadow: 0 6px 18px rgba(0,0,0,.18); }

  /* Letterhead */
  .letterhead {
    left: 70px; top: 50px; width: 560px; height: 792px;
    background: var(--paper); overflow: hidden;
  }
  .letterhead__band {
    position: absolute; left: 0; top: 0; right: 0; height: 180px;
    background: var(--orange);
  }
  .letterhead__stripes {
    position: absolute; left: 0; top: 0; bottom: 0; width: 46px;
    background: repeating-linear-gradient(90deg,
      var(--orange) 0 8px, var(--paper) 8px 15px);
  }
  .letterhead .wordmark { position: absolute; right: 26px; top: 48px; width: 330px; font-size: 30px; }

  /* Wordmark: invented name, one colour, one weight */
  .wordmark {
    font-family: "Montserrat", Arial, sans-serif;
    font-weight: 800; color: var(--paper);
    line-height: 1.05; text-align: right; text-transform: uppercase;
    letter-spacing: .01em;
  }

  /* Envelope */
  .envelope {
    left: 430px; top: 820px; width: 720px; height: 340px;
    background: var(--orange); overflow: hidden;
  }
  .envelope__stripe {
    position: absolute; left: 22px; top: 0; bottom: 0; width: 8px;
    background: var(--paper);
  }
  .envelope .wordmark { position: absolute; right: 40px; top: 90px; width: 380px; font-size: 30px; }

  /* Business cards */
  .card { width: 320px; height: 180px; }
  .card--front {
    left: 700px; top: 560px; background: var(--orange);
  }
  .card--front .wordmark { position: absolute; right: 24px; top: 50px; width: 250px; font-size: 20px; }
  .card--back {
    left: 850px; top: 340px; background: var(--paper);
    padding: 56px 26px 0 0; text-align: right;
  }
  .card__name { color: var(--accent-red); font-weight: 700; font-size: 15px; margin-bottom: 4px; }
  .card__line { color: var(--ink); font-size: 11.5px; line-height: 1.45; }
</style>
</head>
<body>

  <section class="sheet letterhead" aria-label="Letterhead">
    <div class="letterhead__band"></div>
    <div class="letterhead__stripes"></div>
    <p class="wordmark">Bright Anchor Tools and Building Supply Inc.</p>
  </section>

  <section class="sheet card card--back" aria-label="Business card back">
    <p class="card__name">Firstname Lastname</p>
    <p class="card__line">position in the company</p>
    <p class="card__line">tel.: +48 00 000 000</p>
    <p class="card__line">email.: firstnamelastname@mailbox.example</p>
  </section>

  <section class="sheet card card--front" aria-label="Business card front">
    <p class="wordmark">Bright Anchor Tools and Building Supply Inc.</p>
  </section>

  <section class="sheet envelope" aria-label="Envelope">
    <div class="envelope__stripe"></div>
    <p class="wordmark">Bright Anchor Tools and Building Supply Inc.</p>
  </section>

</body>
</html>
```